Restaurant service company needs a website!

I am looking for a skilled web designer/developer to create a professional, responsive, and easy-to-navigate website for my company, which specializes in servicing restaurant cooking equipment. The site should communicate trust, reliability, and technical expertise to our target audience, restaurant owners, managers, and commercial kitchen operators. I have included the company logos, if any other format for them is needed please let me know.

Target Market(s)

restaurant owners, managers, and commercial kitchen operators

Industry/Entity Type

Commercial Kitchen Equipment Service

Coding

Coded - Design and coding required

Number of Pages Required

1 page

Font styles to use
Serif
Sans Serif

Requirements
Must have
• Contact and service request forms, Click-to-call functionality for mobile, Clean, modern layout with strong visuals, Easy navigation, mobile-friendly
Nice to have
• Testimonials or Reviews, If possible a click-to-text functionality for mobile.
Should not have
• Any mention of Refrigeration or HVAC, "Free Quotes"

```html
<!DOCTYPE html>
<html lang="en">
<head>
<meta charset="utf-8">
<title>Waypoint Restaurant Service</title>
<link href="https://fonts.googleapis.com/css2?family=Montserrat:wght@500;600;700;800&family=Poppins:ital,wght@0,400;0,500;0,600;1,400&display=swap" rel="stylesheet">
<style>
:root{
  --teal:#0b5f78;
  --teal-dark:#084b60;
  --ink:#1d1d1f;
  --text:#4a4a4a;
  --blush:#fbf5f4;
  --grey:#f3f2f2;
  --white:#ffffff;
  --line:#e4e0df;
  --star:#f2b51c;
}
*{margin:0;padding:0;box-sizing:border-box}
html,body{width:1200px;height:4914px;overflow:hidden}
body{position:relative;background:var(--blush);font-family:'Poppins',sans-serif;color:var(--text)}
.abs{position:absolute}
.heading{font-family:'Montserrat',sans-serif;font-weight:700;color:var(--teal);line-height:1}
.btn{position:absolute;display:flex;align-items:center;justify-content:center;background:var(--teal);color:var(--white);font-family:'Montserrat',sans-serif;font-weight:700;border-radius:4px;text-decoration:none}
.btn-outline{background:var(--white);color:var(--teal);border:2px solid var(--teal)}

/* header */
.site-header{position:absolute;left:0;top:0;width:1200px;height:160px;background:var(--white)}
.brand{position:absolute;left:65px;top:38px;display:flex;align-items:center;gap:12px}
.brand-mark{width:42px;height:42px;border:3px solid var(--teal)}
.brand-name{font-family:'Montserrat',sans-serif;font-weight:700;color:var(--teal);font-size:38px;line-height:1}
.brand-sub{font-family:'Montserrat',sans-serif;font-weight:700;color:var(--teal);font-size:13px;letter-spacing:4px;margin-top:6px}
.main-nav a{position:absolute;top:100px;font-size:13px;font-weight:500;color:var(--ink);text-decoration:none;text-transform:uppercase}
.main-nav a.active{color:var(--teal)}
.nav-underline{left:493px;top:122px;width:86px;height:2px;background:var(--teal)}

/* hero */
.hero{position:absolute;left:0;top:160px;width:1200px;height:678px}
.hero-photo{position:absolute;inset:0;background:linear-gradient(90deg,#f6f1ef 0%,#eee6e3 45%,#dcd2cd 75%,#cbbfb8 100%)}
.hero-kicker{left:66px;top:300px;font-size:31px}
.hero-rule{left:66px;top:344px;width:104px;height:3px;background:var(--ink)}
.hero-lead{left:66px;top:368px;font-family:'Montserrat',sans-serif;font-weight:600;font-size:34px;color:var(--ink)}
.hero-title{left:64px;top:412px;font-size:74px;letter-spacing:1px}
.hero-title2{left:62px;top:480px;font-family:'Montserrat',sans-serif;font-weight:800;font-size:96px;color:var(--ink);line-height:1}
.hero .btn{left:66px;top:607px;width:294px;height:72px;font-size:22px}

/* about */
.about-frame{left:125px;top:955px;width:440px;height:415px;background:var(--teal);border-radius:110px 0 150px 0}
.about-photo{left:138px;top:965px;width:440px;height:405px;background:linear-gradient(135deg,#3b3b3d,#7a7470 55%,#d9d4d0);border-radius:100px 0 140px 0}
.about-title{left:657px;top:988px;font-size:50px}
.about-lead{left:657px;top:1058px;width:410px;font-size:14px;font-weight:500;color:var(--ink);line-height:27px}
.about-body{left:657px;top:1138px;width:404px;font-size:13px;line-height:27px;text-align:justify}
.about .btn{left:658px;top:1293px;width:166px;height:44px;font-size:13px}

/* features */
.features{position:absolute;left:0;top:1470px;width:1200px;height:372px;background:var(--grey)}
.feature{position:absolute;top:95px;width:240px;text-align:center}
.feature-box{margin:0 auto;width:178px;height:136px;border:2px solid var(--teal);border-radius:4px;padding:7px}
.feature-box div{width:100%;height:100%;background:var(--teal);display:flex;align-items:center;justify-content:center}
.feature-label{margin-top:22px;font-family:'Montserrat',sans-serif;font-weight:700;font-size:19px;color:var(--ink)}

/* services */
.services-title{left:0;top:1947px;width:1200px;text-align:center;font-size:50px}
.services-intro{left:190px;top:2027px;width:820px;text-align:center;font-size:13px;line-height:27px}
.service-card{position:absolute;top:2131px;width:338px}
.service-photo{width:338px;height:339px;border-radius:4px}
.service-name{margin-top:30px;text-align:center;font-family:'Montserrat',sans-serif;font-weight:700;font-size:21px;color:var(--ink)}
.slider-arrow{position:absolute;width:58px;height:58px;border-radius:50%;display:flex;align-items:center;justify-content:center;background:var(--white);box-shadow:0 2px 10px rgba(0,0,0,.15)}
.services .btn{left:508px;top:2588px;width:184px;height:49px;font-size:13px}

/* testimonials */
.testi-title{left:66px;top:2785px;font-size:48px;line-height:1.05}
.round-arrow{position:absolute;width:56px;height:56px;border-radius:50%;display:flex;align-items:center;justify-content:center}
.testi-card{position:absolute;top:2766px;width:322px;height:254px;background:var(--white);box-shadow:0 2px 14px rgba(0,0,0,.09);padding:34px 26px 0 26px}
.testi-text{font-size:13px;font-style:italic;line-height:24px;text-align:justify;color:var(--text)}
.testi-person{display:flex;align-items:center;gap:14px;margin-top:14px}
.avatar{width:62px;height:62px;border-radius:50%;background:linear-gradient(135deg,#c79a72,#6b4b3a);border:3px solid var(--line)}
.testi-name{font-family:'Montserrat',sans-serif;font-weight:700;font-size:18px;color:var(--teal)}
.stars{color:var(--star);font-size:12px;letter-spacing:1px}
.quote-mark{position:absolute;right:22px;bottom:6px;font-family:'Montserrat',sans-serif;font-weight:800;font-size:90px;color:var(--teal);line-height:1}

/* operators */
.operators{position:absolute;left:0;top:3190px;width:1200px;height:592px;background:var(--grey)}
.operators-photo{position:absolute;left:0;top:0;width:800px;height:592px;background:linear-gradient(90deg,#4c5a63 0%,#7d8c95 45%,#b8c0c4 75%,rgba(243,242,242,0) 100%)}
.op-kicker{left:718px;top:3297px;font-family:'Montserrat',sans-serif;font-weight:600;font-size:40px;color:var(--ink)}
.op-title{left:716px;top:3340px;font-size:84px}
.op-title2{left:718px;top:3420px;font-size:58px}
.op-body{left:722px;top:3487px;width:412px;font-size:17px;line-height:33px}
.operators-btn{left:722px;top:3607px;width:384px;height:61px;font-size:20px}

/* contact */
.contact-title{left:93px;top:3950px;font-size:50px}
.field{position:absolute;background:var(--white);border:1px solid var(--line);font-size:13px;color:#9a9a9a;padding:14px 22px}
.submit{left:95px;top:4326px;width:166px;height:42px;font-size:13px}
.contact-frame{left:690px;top:3935px;width:440px;height:410px;background:var(--teal);border-radius:0 150px 0 110px}
.contact-photo{left:678px;top:3948px;width:440px;height:402px;background:linear-gradient(135deg,#2d2d30,#6d6a68 55%,#c9c3be);border-radius:0 140px 0 100px}

/* footer */
.footer-brand{left:218px;top:4578px;width:210px;text-align:center}
.footer-mark{width:96px;height:96px;border:4px solid var(--teal);margin:0 auto 20px}
.footer-name{font-family:'Montserrat',sans-serif;font-weight:700;color:var(--teal);font-size:29px;line-height:1}
.footer-sub{font-family:'Montserrat',sans-serif;font-weight:700;color:var(--teal);font-size:12px;letter-spacing:4px;margin-top:6px}
.footer-head{position:absolute;top:4585px;font-family:'Montserrat',sans-serif;font-weight:600;font-size:19px;color:var(--teal)}
.footer-head::after{content:"";display:block;width:60px;height:2px;background:var(--teal);margin-top:8px}
.quick-links{left:532px;top:4650px;list-style:none;font-size:13px;color:var(--ink);line-height:26px}
.quick-links li::before{content:"";display:inline-block;width:7px;height:7px;border-radius:50%;background:var(--teal);margin-right:13px;vertical-align:middle}
.contact-item{position:absolute;left:791px;display:flex;gap:18px;font-size:13px;color:var(--ink);line-height:17px}
.contact-icon{width:28px;height:28px;background:var(--teal);border-radius:3px;display:flex;align-items:center;justify-content:center;flex:none}
.contact-item b{font-weight:600}

.bottom-bar{position:absolute;left:0;top:4840px;width:1200px;height:74px;background:var(--teal)}
.copyright{left:63px;top:4868px;font-size:11px;color:var(--white)}
.social{position:absolute;top:4862px;width:27px;height:27px;border:1.5px solid var(--white);border-radius:3px}
</style>
</head>
<body>

<header class="site-header">
  <div class="brand">
    <div class="brand-mark"></div>
    <div>
      <div class="brand-name">WAYPOINT</div>
      <div class="brand-sub">RESTAURANT SERVICE</div>
    </div>
  </div>
  <a class="btn btn-outline" style="left:792px;top:30px;width:163px;height:48px;font-size:13px" href="#contact">CONTACT US</a>
  <a class="btn" style="left:967px;top:30px;width:164px;height:48px;font-size:13px" href="#contact">GET A QUOTE</a>
  <nav class="main-nav">
    <a class="active" href="#" style="left:533px">Home</a>
    <a href="#about" style="left:625px">About Us</a>
    <a href="#services" style="left:735px">Services</a>
    <a href="#why" style="left:840px">Why Choose Us</a>
    <a href="#blog" style="left:997px">Blog</a>
    <a href="#reviews" style="left:1076px">Reviews</a>
  </nav>
  <div class="abs nav-underline"></div>
</header>

<section class="hero">
  <div class="hero-photo" role="img" aria-label="Bright commercial kitchen with range hood, hanging utensils and gas stove"></div>
</section>
<div class="abs heading hero-kicker">WAYPOINT</div>
<div class="abs hero-rule"></div>
<div class="abs hero-lead">We Provide the Best &amp; Quality</div>
<div class="abs heading hero-title">RESTAURANT</div>
<div class="abs hero-title2">SERVICES</div>
<section class="hero" style="background:none;pointer-events:auto;top:0;height:0">
  <a class="btn" href="#contact" style="left:66px;top:607px;width:294px;height:72px;font-size:22px">REQUEST SERVICE</a>
</section>

<section class="about" id="about">
  <div class="abs about-frame"></div>
  <div class="abs about-photo" role="img" aria-label="Chef in white jacket checking a commercial oven"></div>
  <h2 class="abs heading about-title">ABOUT US</h2>
  <p class="abs about-lead">Lorem ipsum dolor sit amet, consectetur adipi scing elit, sed do eiusmod tempor incididunt ut labore et</p>
  <p class="abs about-body">Dolore magna aliqua. Quis ipsum suspendisse ultrices gravida. Risus comm odo viverra maecenas accumsan lacus vel facilisis. Lorem ipsum dolor sit amet, consectetur adipiscing elit, sed do eiusmod tempor incididunt ut labore et dolore magna aliqua.</p>
  <a class="btn" href="#" style="left:658px;top:1293px;width:166px;height:44px;font-size:13px">READ MORE</a>
</section>

<section class="features" id="why">
  <div class="feature" style="left:97px">
    <div class="feature-box"><div><svg width="62" height="62" viewBox="0 0 62 62" fill="none" stroke="#fff" stroke-width="3"><circle cx="31" cy="31" r="10"/><circle cx="31" cy="31" r="17" stroke-dasharray="5 4"/><path d="M8 20a25 25 0 0 1 40-10M54 42a25 25 0 0 1-40 10"/><path d="M48 4v7h-7M14 58v-7h7"/></svg></div></div>
    <div class="feature-label">FLEXIBILITY</div>
  </div>
  <div class="feature" style="left:355px">
    <div class="feature-box"><div><svg width="62" height="62" viewBox="0 0 62 62" fill="none" stroke="#fff" stroke-width="3"><circle cx="28" cy="16" r="9"/><circle cx="40" cy="26" r="7"/><path d="M6 44h10l10 4h12l14-8M16 44v10M26 48h8"/></svg></div></div>
    <div class="feature-label">AFFORDABLE PRICING</div>
  </div>
  <div class="feature" style="left:610px">
    <div class="feature-box"><div><svg width="62" height="62" viewBox="0 0 62 62" fill="none" stroke="#fff" stroke-width="3"><circle cx="31" cy="20" r="13"/><path d="M25 20l4 4 8-8M6 46h10l10 4h12l14-8M16 46v10"/></svg></div></div>
    <div class="feature-label">BEST QUALITY</div>
  </div>
  <div class="feature" style="left:863px">
    <div class="feature-box"><div><svg width="66" height="62" viewBox="0 0 66 62" fill="none" stroke="#fff" stroke-width="3"><circle cx="33" cy="16" r="11"/><path d="M28 16l4 4 7-7M4 34l12-6 10 6 7-4 7 4 10-6 12 6M16 28l8 18 9 6 9-6 8-18"/></svg></div></div>
    <div class="feature-label">TRUST WORTHY</div>
  </div>
</section>

<section class="services" id="services">
  <h2 class="abs heading services-title">OUR SERVICES</h2>
  <p class="abs services-intro">Lorem ipsum dolor sit amet, consectetur adipiscing elit, sed do eiusmod tempor incididunt ut labore et dolore magna aliqua. Quis ipsum suspendisse ultrices gravida. Risus comm odo viverra maecenas accumsan lacus vel facilisis.</p>
  <div class="service-card" style="left:70px">
    <div class="service-photo" role="img" aria-label="Technician in apron laying out tools on a workbench" style="background:linear-gradient(160deg,#c9c6c2,#6f6b67 60%,#2e2b29)"></div>
    <div class="service-name">SERVICE 1</div>
  </div>
  <div class="service-card" style="left:432px">
    <div class="service-photo" role="img" aria-label="Hands fitting a whisk to a stand mixer bowl" style="background:linear-gradient(160deg,#9a948f,#4b4643 55%,#c6b6a6)"></div>
    <div class="service-name">SERVICE 2</div>
  </div>
  <div class="service-card" style="left:793px">
    <div class="service-photo" role="img" aria-label="Hand pressing a coffee tamper on a wooden counter" style="background:linear-gradient(160deg,#8f8d8b,#3a3a3b 55%,#c89a66)"></div>
    <div class="service-name">SERVICE 3</div>
  </div>
  <div class="slider-arrow" style="left:43px;top:2275px;background:rgba(255,255,255,.55)"><svg width="14" height="18" viewBox="0 0 14 18" fill="none" stroke="#0b5f78" stroke-width="3"><path d="M10 2 3 9l7 7"/></svg></div>
  <div class="slider-arrow" style="left:1106px;top:2275px"><svg width="14" height="18" viewBox="0 0 14 18" fill="none" stroke="#0b5f78" stroke-width="3"><path d="m4 2 7 7-7 7"/></svg></div>
  <a class="btn" href="#" style="left:508px;top:2588px;width:184px;height:49px;font-size:13px">VIEW ALL SERVICES</a>
</section>

<section class="testimonials" id="reviews">
  <h2 class="abs heading testi-title">OUR<br>TESTIMONIALS</h2>
  <div class="round-arrow" style="left:68px;top:2948px;background:var(--white);box-shadow:0 2px 10px rgba(0,0,0,.15)"><svg width="14" height="18" viewBox="0 0 14 18" fill="none" stroke="#1d1d1f" stroke-width="3"><path d="M10 2 3 9l7 7"/></svg></div>
  <div class="round-arrow" style="left:133px;top:2948px;background:var(--teal)"><svg width="14" height="18" viewBox="0 0 14 18" fill="none" stroke="#fff" stroke-width="3"><path d="m4 2 7 7-7 7"/></svg></div>
  <div class="testi-card" style="left:463px">
    <p class="testi-text">Lorem ipsum dolor sit amet, consecte tur adipiscing elit. Pellentesque aliquet eros vitae placerat hendrerit. Maece nas maximus commodo sapien, vitae lobortis ligula</p>
    <div class="testi-person"><div class="avatar" role="img" aria-label="Customer portrait"></div><div><div class="testi-name">Marcus Hale</div><div class="stars">★★★★★</div></div></div>
    <div class="quote-mark">”</div>
  </div>
  <div class="testi-card" style="left:810px">
    <p class="testi-text">Lorem ipsum dolor sit amet, consecte tur adipiscing elit. Pellentesque aliquet eros vitae placerat hendrerit. Maece nas maximus commodo sapien, vitae lobortis ligula</p>
    <div class="testi-person"><div class="avatar" role="img" aria-label="Customer portrait" style="background:linear-gradient(135deg,#e6c59c,#b07a52)"></div><div><div class="testi-name">Priya Lorne</div><div class="stars">★★★★★</div></div></div>
    <div class="quote-mark">”</div>
  </div>
</section>

<section class="operators">
  <div class="operators-photo" role="img" aria-label="Two technicians in masks and gloves servicing a gas range"></div>
</section>
<div class="abs op-kicker">COMMERCIAL</div>
<div class="abs heading op-title">KITCHEN</div>
<div class="abs heading op-title2">OPERATORS</div>
<p class="abs op-body">Lorem ipsum dolor sit amet, consectetur adip isicing elit, sed do eius mod tempor incididunt ut labore et dolore magna aliqua.</p>
<a class="btn operators-btn" href="#contact">REQUEST YOUR SERVICE TYPE</a>

<section class="contact" id="contact">
  <h2 class="abs heading contact-title">CONTACT US</h2>
  <div class="field" style="left:92px;top:4036px;width:258px;height:49px">First Name:</div>
  <div class="field" style="left:373px;top:4036px;width:258px;height:49px">Last Name:</div>
  <div class="field" style="left:92px;top:4103px;width:258px;height:49px">Phone:</div>
  <div class="field" style="left:373px;top:4103px;width:258px;height:49px">Email:</div>
  <div class="field" style="left:92px;top:4173px;width:539px;height:121px">Message:</div>
  <a class="btn submit" href="#">SUBMIT NOW</a>
  <div class="abs contact-frame"></div>
  <div class="abs contact-photo" role="img" aria-label="Technician repairing a commercial oven with a multimeter"></div>
</section>

<footer>
  <div class="abs footer-brand">
    <div class="footer-mark"></div>
    <div class="footer-name">WAYPOINT</div>
    <div class="footer-sub">RESTAURANT SERVICE</div>
  </div>
  <div class="footer-head" style="left:532px">QUICK LINKS</div>
  <ul class="abs quick-links">
    <li>About Us</li><li>Services</li><li>Why Choose Us</li><li>Reviews</li><li>Contact Us</li>
  </ul>
  <div class="footer-head" style="left:791px">CONTACT US</div>
  <div class="contact-item" style="top:4648px"><div class="contact-icon"><svg width="14" height="14" viewBox="0 0 14 14" fill="#fff"><path d="M3 1l2 3-1.5 1.5a8 8 0 0 0 5 5L10 9l3 2-1 2.5C6 14 0 8 .5 2z"/></svg></div><div><b>CALL US</b><br>8012 555 0147</div></div>
  <div class="contact-item" style="top:4702px"><div class="contact-icon"><svg width="14" height="11" viewBox="0 0 14 11" fill="none" stroke="#fff" stroke-width="1.5"><rect x="1" y="1" width="12" height="9"/><path d="m1 1 6 5 6-5"/></svg></div><div><b>EMAIL US</b><br>info@yoursitename.com</div></div>
  <div class="contact-item" style="top:4754px"><div class="contact-icon"><svg width="12" height="15" viewBox="0 0 12 15" fill="#fff"><path d="M6 0a6 6 0 0 1 6 6c0 4-6 9-6 9S0 10 0 6a6 6 0 0 1 6-6zm0 3.5a2.5 2.5 0 1 0 0 5 2.5 2.5 0 0 0 0-5z"/></svg></div><div>Address line dummy here'<br>Addres line dummy here</div></div>

  <div class="bottom-bar"></div>
  <div class="abs copyright">Copyright © 2025 All Rights Reserved By Company name</div>
  <div class="social" style="left:1010px"></div>
  <div class="social" style="left:1042px"></div>
  <div class="social" style="left:1073px"></div>
  <div class="social" style="left:1104px"></div>
</footer>

</body>
</html>
```